We need a flyer where we promote a workshop to our members of the jewish community www.qvb-gemeinde.example . The workshop is calles "guidance in ten seasons presented by QVB. We would like to see a flyer with the below text is used and also some pictures (attached). The flyer should come over as cool, fresh, innovative for a younger crowd so called young professionals (age 28-35).
TITLE.
"Guidance in Ten Seasons.
SUBTITLE.
Your systematic self-coaching roadmap to power and impact—and your future.”
TEXT.
Dr. Martin K. Halvorsen is the CEO Emeritus of Alpine Advisory Partners—he made an exit in 2013. He is the award-winning author of 8 books, including "Plan-Into-Motion," "Speak or Falter" and "The Cantor and the Chairman.”
For the past 20 years he has taught leadership at Harwick University in New York and at BKU (Lindenberg University) to prepare future CEOs and other leaders in business, government , nonprofits and the military.
Now, in a process exclusively designed for QVB’s next generation of emerging leaders, Martin unpacks his leadership secrets in 3 action-packed labs—reduced to the max:
Lab 1. Guidance in Ten Seasons: The Summit Guide Triangle®. Self-Assessment. Self-Leadership: “The Lantern.” 5-Year Vision. 100-Day Catalytic Project.
Lab 2. Leading Through Language. Relationship: Building Trust. Plan-Into-Motion. Cockpit.
Lab 3. Debrief and Scale-Up. Sustainability. Action Tools.
Do you want to build your own future and a life you love? Do you want to jump-start that future and life over 100 days while learning a toolbox of leadership skills, networking with like-minded people—and even get some pizza? Then join us.
Target Market(s)
young professionals age 28-35

```html
<!DOCTYPE html>
<html lang="en">
<head>
<meta charset="utf-8">
<title>Guidance in Ten Seasons — QVB Workshop Flyer</title>
<link rel="stylesheet" href="https://fonts.googleapis.com/css2?family=Bebas+Neue&family=Poppins:wght@400;500;600;700&display=swap">
<style>
  :root{
    --page-bg:#c9cccb;
    --ink:#111111;
    --night:#050505;
    --white:#ffffff;
    --sky-top:#ee8a0c;
    --sky-mid:#f6a622;
    --sky-low:#f07a12;
    --ember:#e8330e;
    --crimson:#c81d12;
    --teal:#4fd0c2;
    --cta-red:#c4161c;
    --link-blue:#1ea3dc;
    --brand-blue:#1f3a9c;
    --rule:#777777;
  }
  *{box-sizing:border-box;margin:0;padding:0}
  html,body{width:972px;height:1200px;overflow:hidden;background:var(--page-bg)}
  .flyer-frame{position:absolute;left:62px;top:0;width:848px;height:1200px;overflow:hidden}
  .flyer{position:absolute;left:0;top:0;width:1166px;height:1650px;transform:scale(0.72727);transform-origin:0 0;font-family:'Poppins',sans-serif;color:var(--white)}
  .flyer-art{position:absolute;inset:0}
  .title-block{font-weight:400}
  .title{position:absolute;left:0;width:1166px;text-align:center;font-family:'Bebas Neue',sans-serif;color:var(--white);line-height:1;white-space:nowrap;text-shadow:3px 3px 0 rgba(0,0,0,.35)}
  .title-top{top:86px;font-size:186px;letter-spacing:1px}
  .title-mid{top:232px;font-size:100px}
  .title-bottom{top:343px;font-size:190px;letter-spacing:-1px}
  .subtitle{position:absolute;top:548px;left:222px;width:720px;text-align:center;font-weight:700;font-size:30px;line-height:1.38}
  .bio{position:absolute;left:56px;top:656px;width:1060px;list-style:none}
  .bio li{position:relative;padding-left:42px;font-size:21.5px;line-height:1.38;margin-bottom:26px}
  .bio li svg,.labs li svg{position:absolute;left:0;top:7px;width:21px;height:21px}
  .name{color:var(--teal);font-weight:600}
  .book{font-weight:700}
  .labs{position:absolute;left:418px;top:982px;width:690px;list-style:none}
  .labs li{position:relative;padding-left:40px;font-size:21.5px;line-height:1.38;margin-bottom:28px}
  .labs li svg{top:6px}
  .lab-label{color:var(--ember);font-weight:600}
  .cta{position:absolute;left:555px;top:1312px;width:580px;text-align:center;color:var(--ink)}
  .cta-heading{color:var(--cta-red);font-weight:700;font-size:32px;line-height:1.3;margin:0 auto 10px;width:520px}
  .cta-body{font-size:21px;line-height:1.5}
  .highlight{color:var(--link-blue);font-weight:600}
  .rule{position:absolute;left:542px;top:1549px;width:624px;height:2px;background:var(--rule)}
  .contact{position:absolute;right:210px;top:1582px;font-size:26px;letter-spacing:1px;color:#2a2a2a;white-space:nowrap}
  .contact .domain{color:var(--brand-blue)}
  .brand{position:absolute;left:984px;top:1568px;font-weight:700;font-size:58px;color:var(--brand-blue);line-height:1}
</style>
</head>
<body>
<div class="flyer-frame">
  <div class="flyer">
    <svg class="flyer-art" width="1166" height="1650" viewBox="0 0 1166 1650">
      <defs>
        <linearGradient id="sky" x1="0" y1="0" x2="0.4" y2="1">
          <stop offset="0" stop-color="var(--sky-top)"/>
          <stop offset="0.3" stop-color="var(--sky-mid)"/>
          <stop offset="0.6" stop-color="var(--sky-low)"/>
          <stop offset="0.85" stop-color="var(--ember)"/>
        </linearGradient>
        <linearGradient id="band" x1="0" y1="0" x2="1" y2="1">
          <stop offset="0" stop-color="var(--ember)"/>
          <stop offset="1" stop-color="var(--crimson)"/>
        </linearGradient>
        <linearGradient id="portrait" x1="0" y1="0" x2="0" y2="1">
          <stop offset="0" stop-color="#c9a48c"/>
          <stop offset="0.4" stop-color="#b38a74"/>
          <stop offset="0.5" stop-color="#4b4f55"/>
          <stop offset="1" stop-color="#3a3d42"/>
        </linearGradient>
      </defs>
      <rect class="sky" width="1166" height="760" fill="url(#sky)"/>
      <polygon class="ridge" fill="var(--night)" points="0,455 90,425 170,412 230,440 300,480 390,525 470,560 560,590 680,630 790,652 900,690 1000,700 1166,725 1166,1650 0,1650"/>
      <rect class="summit-figure" role="img" aria-label="Silhouette of a person holding a flag atop a rocky summit" x="47" y="55" width="235" height="300" rx="12" fill="#2a1407" opacity="0.85"/>
      <polygon class="accent-band" fill="url(#band)" points="0,1133 652,1285 422,1322 422,1650 0,1650"/>
      <polygon class="cta-panel" fill="var(--white)" points="422,1322 1166,1205 1166,1650 422,1650"/>
      <polygon class="speaker-portrait" role="img" aria-label="Portrait photo of the speaker in a grey suit, arms crossed" fill="url(#portrait)" points="125,1015 315,1015 315,1250 470,1290 560,1650 0,1650 0,1255 125,1255"/>
    </svg>

    <h1 class="title-block">
      <span class="title title-top">GUIDANCE</span>
      <span class="title title-mid">IN</span>
      <span class="title title-bottom">TEN SEASONS</span>
    </h1>

    <p class="subtitle">Your systematic self-coaching roadmap to power and impact—and your future.</p>

    <ul class="bio">
      <li><svg viewBox="0 0 20 20"><circle cx="10" cy="10" r="10" fill="var(--teal)"/><path d="M5.5 10.2l3 3 6-6" stroke="var(--night)" stroke-width="2.4" fill="none"/></svg><span class="name">Dr. Martin K. Halvorsen</span> is the CEO Emeritus of Alpine Advisory Partners—he made an exit in 2013. He is the award-winning author of 8 books, including "<span class="book">Plan-Into-Motion</span>," "<span class="book">Speak or Falter</span>" and "<span class="book">The Cantor and the Chairman.</span>”</li>
      <li><svg viewBox="0 0 20 20"><circle cx="10" cy="10" r="10" fill="var(--teal)"/><path d="M5.5 10.2l3 3 6-6" stroke="var(--night)" stroke-width="2.4" fill="none"/></svg>For the past 20 years he has taught leadership at Harwick University in New York and at BKU (Lindenberg University) to prepare future CEOs and other leaders in business, government , nonprofits and the military.</li>
      <li><svg viewBox="0 0 20 20"><circle cx="10" cy="10" r="10" fill="var(--teal)"/><path d="M5.5 10.2l3 3 6-6" stroke="var(--night)" stroke-width="2.4" fill="none"/></svg>Now, in a process exclusively designed for QVB’s next generation of emerging leaders, Martin unpacks his leadership secrets in 3 action-packed labs—reduced to the max:</li>
    </ul>

    <ul class="labs">
      <li><svg viewBox="0 0 20 20"><circle cx="10" cy="10" r="10" fill="var(--ember)"/><path d="M5.5 10.2l3 3 6-6" stroke="var(--white)" stroke-width="2.4" fill="none"/></svg><span class="lab-label">Lab 1.</span> Guidance in Ten Seasons: The Summit Guide Triangle®. Self-Assessment. Self-Leadership: “The Lantern.” 5-Year Vision. 100-Day Catalytic Project.</li>
      <li><svg viewBox="0 0 20 20"><circle cx="10" cy="10" r="10" fill="var(--ember)"/><path d="M5.5 10.2l3 3 6-6" stroke="var(--white)" stroke-width="2.4" fill="none"/></svg><span class="lab-label">Lab 2.</span> Leading Through Language. Relationship: Building Trust. Plan-Into-Motion. Cockpit.</li>
      <li><svg viewBox="0 0 20 20"><circle cx="10" cy="10" r="10" fill="var(--ember)"/><path d="M5.5 10.2l3 3 6-6" stroke="var(--white)" stroke-width="2.4" fill="none"/></svg><span class="lab-label">Lab 3.</span> Debrief and Scale-Up. Sustain ability. Action Tools.</li>
    </ul>

    <div class="cta">
      <h2 class="cta-heading">Do you want to build your own future and a life you love?</h2>
      <p class="cta-body">Do you want to jump-start that future and life<br><span class="highlight">over 100 days</span> while learning a toolbox of leadership skills, networking with like-minded people—and even get some pizza? Then join us.</p>
    </div>

    <div class="rule"></div>
    <div class="contact">www.<span class="domain">qvb-gemeinde</span>.example</div>
    <div class="brand">QVB</div>
  </div>
</div>
</body>
</html>
```